Cedar Row Maintenance and Concierge Flyer

We need a flyer for cedar row maintenance and concierge service. We specialize in and provide residential maintenance and errand services to retired and semi retired persons living in the Lake Norman area. The services we include:
Lighting and plumbing repairs
Ceiling fan installation
Handicap accessories
Locks and security
Picture hanging
Hang blinds
Furniture arrangement / assembly
Pressure washing
Battery Jump start
and more...

Our Concierge services include:
Errand running
Grocery shopping
Wellness Checks
Dog Walk
Garbage Collection
and more...

We offer monthly service agreements and 24/7 access
Call text or e-mail for more information
704.555.0187
1cedarrowmaint@quillpostmail.com

The design should invoke a sense of trust and a customer service driven mission

Target Market(s)

Residential maintenance

Industry/Entity Type

Property Maintenance

Contact Information for Business Card

Derek Halvorsen
48176 Quimby Ferrel Rd.
Cornelius NC 28031
704.555.0187
with uploaded logo

Requirements
Nice to have
• Would like a postcard size flyer. Front and back
Should not have
• No pics of of people wearing hard hats or pics of blueprints. No pics of commercial or industrial maintenance.

```html
<!DOCTYPE html>
<html lang="en">
<head>
<meta charset="utf-8">
<title>Cedar Row Maintenance &amp; Concierge — Flyer Front</title>
<link href="https://fonts.googleapis.com/css2?family=Questrial&family=Pompiere&display=swap" rel="stylesheet">
<style>
  :root {
    --red: #d2232a;
    --ink: #1a1a1a;
    --grey: #6d6e71;
    --paper: #ffffff;
    --shadow: rgba(0,0,0,.75);
  }
  html, body { margin: 0; padding: 0; overflow: hidden; background: var(--paper); }
  .flyer {
    position: relative; width: 720px; height: 1200px; overflow: hidden;
    background: var(--paper); font-family: "Questrial", sans-serif; color: var(--ink);
  }
  .flyer > * { position: absolute; margin: 0; }
  .accents { left: 0; top: 0; }

  .brand { left: 28px; top: 44px; display: flex; align-items: center; gap: 14px; }
  .brand-dot { width: 62px; height: 62px; border-radius: 50%; background: var(--grey); }
  .brand-name { font-size: 30px; color: var(--grey); line-height: 1.05; }
  .brand-name small { display: block; font-size: 15px; letter-spacing: .5px; }

  .script { font-family: "Pompiere", "Arial Narrow", sans-serif; font-weight: 400; white-space: nowrap; line-height: 1; }
  .section-title { color: var(--red); text-align: right; }
  .title-specialized { right: 347px; top: 190px; font-size: 52px; }
  .title-maintenance { right: 340px; top: 752px; font-size: 32px; }

  .intro {
    right: 348px; top: 246px; white-space: nowrap;
    text-align: right; font-size: 21.5px; line-height: 28px;
  }
  .service-list {
    right: 342px; top: 793px; padding: 0; list-style: none; white-space: nowrap;
    text-align: right; font-size: 20.5px; line-height: 26px;
  }
  .service-list .more { color: var(--red); margin-top: 2px; }

  .photo { box-shadow: 16px 16px 12px var(--shadow); }
  .photo-plumbing { left: 454px; top: 25px; width: 224px; height: 208px;
    background: linear-gradient(160deg, #c98a5e 0%, #b9764c 55%, #9aa3ab 70%, #2e5a8c 100%); }
  .photo-handicap { left: 396px; top: 294px; width: 226px; height: 200px;
    background: linear-gradient(180deg, #d9dde0 0%, #b8bec4 45%, #f2f2f2 70%, #c9cdd0 100%); }
  .photo-furniture { left: 398px; top: 570px; width: 223px; height: 200px;
    background: linear-gradient(135deg, #f1ede6 0%, #e6dfd3 50%, #b48a5c 100%); }
  .photo-blinds { left: 454px; top: 853px; width: 224px; height: 198px;
    background: linear-gradient(90deg, #e9ead8 0%, #f7f7f2 30%, #7f9a6a 55%, #f4f4ee 80%, #e4e2cf 100%); }
  .badge-security { left: 136px; top: 444px; width: 194px; height: 182px; background: #fff;
    box-shadow: 16px 16px 12px var(--shadow);
    display: flex; align-items: center; justify-content: center; }
  .badge-security span { width: 176px; height: 176px; border-radius: 50%;
    background: radial-gradient(circle at 50% 35%, #3f8ee8 0%, #1145b8 60%, #0a2a78 100%); }

  .caption { font-size: 29px; color: var(--ink); }
  .cap-plumbing { left: 512px; top: 256px; }
  .cap-handicap { left: 426px; top: 516px; }
  .cap-security { left: 158px; top: 666px; }
  .cap-furniture { left: 434px; top: 792px; }
  .cap-blinds { left: 482px; top: 1062px; }

  .see-back { right: 36px; top: 1154px; font-size: 31px; color: var(--red); }
</style>
</head>
<body>
<main class="flyer">
  <svg class="accents" width="720" height="1200" viewBox="0 0 720 1200" aria-hidden="true">
    <g fill="none" stroke="#d2232a">
      <path d="M30 237 H386 M385 186 V414" stroke-width="3"/>
      <path d="M30 788 H386 M385 752 V1112" stroke-width="3"/>
      <path d="M510 568 C610 555 700 610 724 700" stroke-width="10"/>
      <path d="M385 1112 C470 1140 640 1140 724 1030" stroke-width="10"/>
    </g>
  </svg>

  <div class="brand">
    <span class="brand-dot"></span>
    <div class="brand-name">Cedar Row<small>MAINTENANCE &amp; CONCIERGE</small></div>
  </div>

  <h1 class="section-title title-specialized script">Specialized Services</h1>
  <p class="intro">We specialize in and provide<br>residential maintenance and<br>errand services to retired and<br>semi retired persons living in<br>the Lake Norman area.</p>

  <div class="photo photo-plumbing" role="img" aria-label="Photo of hands repairing a chrome sink drain pipe"></div>
  <span class="caption script cap-plumbing">plumbing repairs</span>

  <div class="photo photo-handicap" role="img" aria-label="Photo of a tiled bathroom with toilet and grab bars"></div>
  <span class="caption script cap-handicap">handicap accessories</span>

  <div class="badge-security" role="img" aria-label="Blue round security badge with a padlock icon"><span></span></div>
  <span class="caption script cap-security">locks and security</span>

  <div class="photo photo-furniture" role="img" aria-label="Photo of hands assembling white furniture panels with a screwdriver"></div>
  <span class="caption script cap-furniture">furniture assembly</span>

  <div class="photo photo-blinds" role="img" aria-label="Photo of a hand installing window blinds"></div>
  <span class="caption script cap-blinds">maintenance projects</span>

  <h2 class="section-title title-maintenance script">Our maintenance services includes:</h2>
  <ul class="service-list">
    <li>Lighting and plumbing repairs</li>
    <li>Ceiling fan installation</li>
    <li>Handicap accessories</li>
    <li>Locks and security</li>
    <li>Picture hanging</li>
    <li>Hang blinds</li>
    <li>Furniture arrangement/assembly</li>
    <li>Pressure washing</li>
    <li>Battery Jump start</li>
    <li class="more">and more...</li>
  </ul>

  <p class="see-back script">see back for more information...</p>
</main>
</body>
</html>
```